Radiant Harvest Gathering 2021

I am looking to create a flyer for a one day prayer retreat our church is organizing. This flyer will be posted on social media, websites, mobile apps, and will also be printed so it can be mailed to people.

I am looking for something professional, with good use of our logo and band colors (logo colors).

I am counting on the designer's skill, creativity, art and knowledge of media communication to produce a flyer that will effectively and quickly convey the message we are trying to spread.

CONTENT OF THE FLYER:
Event title: Radiant Harvest Gathering
Date: Tuesday July 2nd, 2021
Time: 11:00AM - 7:00PM
Bellmore Hotel, 4817 Wexley Avenue, Portland, Maine 04109 (Room: Tamarind)
Event Key words to highlight what the event is about: Prayer, Fasting, Worship, Prophecy, Revival.
Key phrases:
A one day prayer retreat.
Jesus Chris is Lord

Contact info:
www.quvello.org
Phone: 207 555 0148
Email: contact@brookmeadow.org

```html
<!DOCTYPE html>
<html lang="en">
<head>
<meta charset="utf-8">
<title>Radiant Harvest Gathering 2021</title>
<link rel="stylesheet" href="https://fonts.googleapis.com/css2?family=Cinzel:wght@500;600&family=Arimo:wght@400;700&family=Open+Sans:wght@400;600&family=Tinos:wght@700&display=swap">
<style>
  :root {
    --page: #e6e6e6;
    --ink-dark: #1a0e0b;
    --brown-deep: #2a1712;
    --brown-mid: #4a2c22;
    --glow: #c98a55;
    --orange: #f39a1e;
    --orange-dark: #c9720d;
    --white: #ffffff;
  }
  * { margin: 0; padding: 0; box-sizing: border-box; }
  html, body { width: 1200px; height: 1200px; overflow: hidden; background: var(--page); }
  .flyer {
    position: absolute; left: 60px; top: 240px;
    width: 1080px; height: 720px;
    background: var(--brown-deep);
    overflow: hidden;
  }
  .flyer-photo {
    position: absolute; inset: 0;
    background:
      radial-gradient(ellipse 300px 260px at 640px 250px, rgba(255,196,120,0.75), rgba(201,138,85,0.25) 55%, transparent 80%),
      radial-gradient(ellipse 420px 220px at 720px 520px, rgba(214,160,110,0.55), transparent 75%),
      linear-gradient(90deg, var(--ink-dark) 0%, var(--brown-deep) 35%, var(--brown-mid) 70%, #3a221a 100%);
  }
  .info {
    position: absolute; left: 90px; top: 30px; width: 440px;
    text-align: center; color: var(--white);
  }
  .brand {
    display: flex; align-items: center; justify-content: center; gap: 12px;
    font-family: 'Cinzel', serif; font-weight: 600; font-size: 42px; line-height: 1.2;
    color: var(--white); letter-spacing: 2px;
  }
  .brand-dot { width: 20px; height: 20px; border-radius: 50%; background: var(--orange); }
  .title { margin-top: 16px; font-family: 'Cinzel', serif; font-weight: 500; line-height: 1; }
  .title-top { display: block; font-size: 40px; color: var(--white); }
  .title-main { display: block; font-size: 58px; color: var(--orange); margin-top: 8px; }
  .divider { display: block; margin: 12px auto; }
  .when { font-family: 'Arimo', sans-serif; font-weight: 700; font-size: 26px; line-height: 1.4; }
  .retreat {
    position: relative; margin: 28px auto 0; width: 380px;
    border: 2px solid var(--orange); padding: 30px 20px 16px;
  }
  .retreat-tag {
    position: absolute; top: -18px; left: 24px;
    background: var(--orange); color: var(--white);
    font-family: 'Tinos', serif; font-weight: 700; font-size: 21px;
    padding: 4px 18px;
  }
  .keywords { font-family: 'Arimo', sans-serif; font-weight: 700; font-size: 19px; line-height: 1.4; }
  .venue {
    margin-top: 14px; font-family: 'Arimo', sans-serif; font-weight: 400;
    font-size: 16px; line-height: 1.35;
  }
  .contact-band {
    position: absolute; left: 0; right: 0; top: 596px; height: 64px;
    background: linear-gradient(90deg, var(--orange-dark), var(--orange) 30%, var(--orange));
    display: flex; align-items: center; justify-content: flex-end; padding-right: 40px;
    font-family: 'Open Sans', sans-serif; font-size: 32px; color: var(--ink-dark);
  }
  .contact-band strong { font-weight: 600; }
  .contact-band .sep { margin: 0 14px; }
  .base-strip { position: absolute; left: 0; right: 0; top: 660px; bottom: 0; background: var(--ink-dark); }
</style>
</head>
<body>
  <main class="flyer">
    <div class="flyer-photo" role="img" aria-label="Photograph of a lit candle beside an open Bible with hands folded in prayer, in warm candlelight"></div>

    <section class="info">
      <div class="brand"><span class="brand-dot"></span>QUVELLO</div>

      <h1 class="title">
        <span class="title-top">RADIANT HARVEST</span>
        <span class="title-main">GATHERING</span>
      </h1>

      <svg class="divider" width="300" height="10" viewBox="0 0 300 10" aria-hidden="true">
        <line x1="0" y1="5" x2="300" y2="5" stroke="#f39a1e" stroke-width="2"/>
      </svg>

      <p class="when">Date: Tuesday July 2nd, 2021<br>Time: 11:00AM - 7:00PM</p>

      <svg class="divider" width="300" height="10" viewBox="0 0 300 10" aria-hidden="true">
        <line x1="0" y1="5" x2="300" y2="5" stroke="#f39a1e" stroke-width="2"/>
      </svg>

      <div class="retreat">
        <span class="retreat-tag">A one day prayer retreat</span>
        <p class="keywords">Prayer, Fasting, Worship,<br>Prophecy, Revival.</p>
      </div>

      <p class="venue">Bellmore Hotel, 4817 Wexley Avenue, Portland, Maine<br>04109 (Room: Tamarind)</p>
    </section>

    <footer class="contact-band">
      <span>www.<strong>quvello</strong>.org</span><span class="sep">|</span><span>207 555 0148</span><span class="sep">|</span><span>contact@brookmeadow.org</span>
    </footer>
    <div class="base-strip"></div>
  </main>
</body>
</html>
```